Diagram of Marrowfen’s history for website

This project is to design the attached diagram along the lines of the attached image but in our branding - style guide attached. The diagram will be going on the Marrowfen website - www.marrowfen.au.

```html
<!DOCTYPE html>
<html lang="en">
<head>
<meta charset="utf-8">
<title>Marrowfen – Our History</title>
<link href="https://fonts.googleapis.com/css2?family=Montserrat:wght@400;700;800&display=swap" rel="stylesheet">
<style>
  :root {
    --bg: #ffffff;
    --brown: #6b5a4c;
    --brown-text: #8a7465;
    --slate: #3c4856;
    --slate-text: #5b6673;
    --sage: #4e5f58;
    --sage-text: #6d7d77;
    --panel: #ececec;
    --ribbon-dark: #3f5870;
    --ribbon-light: #8aa0b4;
    --fold: #c9ac94;
  }
  * { box-sizing: border-box; margin: 0; padding: 0; }
  html, body { width: 1200px; height: 1200px; overflow: hidden; background: var(--bg); }
  body { font-family: "Montserrat", sans-serif; position: relative; }

  .timeline { position: absolute; inset: 0; }

  .year-panel { position: absolute; }
  .year-panel.above { background: linear-gradient(to bottom, rgba(236,236,236,0) 0%, var(--panel) 100%); }
  .year-panel.below { background: linear-gradient(to top, rgba(236,236,236,0) 0%, var(--panel) 100%); }

  .ribbon { position: absolute; left: 0; top: 0; width: 1200px; height: 1200px; }

  .year {
    position: absolute;
    font-weight: 800;
    font-size: 73px;
    line-height: 1;
    letter-spacing: -1px;
  }

  .milestones { position: absolute; display: flex; flex-direction: column; gap: 14px; }
  .milestone h2 { font-weight: 700; font-size: 19px; line-height: 21px; letter-spacing: 0.2px; margin-bottom: 6px; }
  .milestone p { font-weight: 400; font-size: 14.5px; line-height: 17.4px; letter-spacing: 0.3px; }

  .tone-brown h2, .tone-brown.year { color: var(--brown); }
  .tone-brown p { color: var(--brown-text); }
  .tone-slate h2, .tone-slate.year { color: var(--slate); }
  .tone-slate p { color: var(--slate-text); }
  .tone-sage h2, .tone-sage.year { color: var(--sage); }
  .tone-sage p { color: var(--sage-text); }
</style>
</head>
<body>
<main class="timeline">

  <div class="year-panel above" style="left:103px;top:450px;width:217px;height:150px"></div>
  <div class="year-panel above" style="left:393px;top:450px;width:217px;height:150px"></div>
  <div class="year-panel above" style="left:659px;top:455px;width:265px;height:145px"></div>
  <div class="year-panel below" style="left:248px;top:608px;width:217px;height:152px"></div>
  <div class="year-panel below" style="left:538px;top:608px;width:217px;height:152px"></div>
  <div class="year-panel below" style="left:803px;top:608px;width:266px;height:152px"></div>

  <svg class="ribbon" viewBox="0 0 1200 1200" aria-hidden="true">
    <defs>
      <linearGradient id="ribbon-fill" x1="103" y1="0" x2="1103" y2="0" gradientUnits="userSpaceOnUse">
        <stop offset="0" stop-color="#8aa0b4"/>
        <stop offset="0.109" stop-color="#3f5870"/>
        <stop offset="0.18" stop-color="#8aa0b4"/>
        <stop offset="0.253" stop-color="#3f5870"/>
        <stop offset="0.325" stop-color="#8aa0b4"/>
        <stop offset="0.399" stop-color="#3f5870"/>
        <stop offset="0.47" stop-color="#8aa0b4"/>
        <stop offset="0.544" stop-color="#3f5870"/>
        <stop offset="0.615" stop-color="#8aa0b4"/>
        <stop offset="0.689" stop-color="#3f5870"/>
        <stop offset="0.76" stop-color="#8aa0b4"/>
        <stop offset="0.833" stop-color="#3f5870"/>
        <stop offset="0.91" stop-color="#8aa0b4"/>
        <stop offset="1" stop-color="#3f5870"/>
      </linearGradient>
      <linearGradient id="fold-up" x1="0" y1="1" x2="0" y2="0">
        <stop offset="0" stop-color="#ffffff" stop-opacity="0"/>
        <stop offset="1" stop-color="#c9ac94"/>
      </linearGradient>
      <linearGradient id="fold-down" x1="0" y1="0" x2="0" y2="1">
        <stop offset="0" stop-color="#ffffff" stop-opacity="0"/>
        <stop offset="1" stop-color="#c9ac94"/>
      </linearGradient>
    </defs>
    <polygon points="60,628 103,622 103,632" fill="#eeeeee"/>
    <g class="folds">
      <polygon points="140,590 212,560 285,590 212,576" fill="url(#fold-up)"/>
      <polygon points="430,590 502,560 575,590 502,576" fill="url(#fold-up)"/>
      <polygon points="720,590 792,560 865,590 792,576" fill="url(#fold-up)"/>
      <polygon points="285,615 356,647 430,615 356,632" fill="url(#fold-down)"/>
      <polygon points="575,615 647,647 720,615 647,632" fill="url(#fold-down)"/>
      <polygon points="865,615 936,647 1008,615 936,632" fill="url(#fold-down)"/>
      <polyline points="140,588 212,560 285,588" fill="none" stroke="#ffffff" stroke-width="2"/>
      <polyline points="430,588 502,560 575,588" fill="none" stroke="#ffffff" stroke-width="2"/>
      <polyline points="720,588 792,560 865,588" fill="none" stroke="#ffffff" stroke-width="2"/>
      <polyline points="285,617 356,648 430,617" fill="none" stroke="#ffffff" stroke-width="2"/>
      <polyline points="575,617 647,648 720,617" fill="none" stroke="#ffffff" stroke-width="2"/>
      <polyline points="865,617 936,648 1008,617" fill="none" stroke="#ffffff" stroke-width="2"/>
    </g>
    <polygon fill="url(#ribbon-fill)" points="103,594 212,575 356,603 502,575 647,603 792,575 936,603 1081,578 1081,562 1103,584 1081,612 1081,609 936,632 792,603 647,632 502,603 356,632 212,603 103,625"/>
  </svg>

  <div class="year tone-brown" style="left:128px;top:478px">2017</div>
  <div class="year tone-slate" style="left:417px;top:478px">2019</div>
  <div class="year tone-sage" style="left:701px;top:473px">2022</div>
  <div class="year tone-sage" style="left:271px;top:667px">2018</div>
  <div class="year tone-brown" style="left:562px;top:667px">2021</div>
  <div class="year tone-slate" style="left:843px;top:662px">2023</div>

  <section class="milestones tone-brown" style="left:123px;top:193px;width:200px;gap:19px">
    <article class="milestone">
      <h2>Marrowfen<br>Commences</h2>
      <p>Maren started the business with 25 years’ experience working for government &amp; non-government disability &amp; community services. Our first office is in Preston</p>
    </article>
    <article class="milestone">
      <h2>NDIS Provider</h2>
      <p>Marrowfen becomes a NDIS Registered provider</p>
    </article>
  </section>

  <section class="milestones tone-slate" style="left:412px;top:340px;width:160px">
    <article class="milestone">
      <h2>Move to<br>Alphington</h2>
      <p>Marrowfen moves to Alphington due to further growth &amp; expansion</p>
    </article>
  </section>

  <section class="milestones tone-sage" style="left:678px;top:163px;width:250px;gap:18px">
    <article class="milestone">
      <h2>Corvella Best of<br>Business</h2>
      <p>Marrowfen wins the Corvella Best of Business Award (Vic) for building communities</p>
    </article>
    <article class="milestone">
      <h2>Move to Coburg</h2>
      <p>Marrowfen moves to a larger premises in Coburg</p>
    </article>
    <article class="milestone">
      <h2>Partnerships</h2>
      <p>Partnerships established with Tarawen School for Children with Disability &amp; Yarrang Circle (Eastbrook University)</p>
    </article>
  </section>

  <section class="milestones tone-sage" style="left:267px;top:750px;width:190px">
    <article class="milestone">
      <h2>Clinic Expansion</h2>
      <p>Marrowfen moves offices twice in Preston due to growth &amp; expansion. Clinic established</p>
    </article>
  </section>

  <section class="milestones tone-brown" style="left:557px;top:750px;width:200px">
    <article class="milestone">
      <h2>B-Corporation</h2>
      <p>Marrowfen becomes a accredited B-Corporation having met the highest standards of environmental social &amp; community performance</p>
    </article>
  </section>

  <section class="milestones tone-slate" style="left:823px;top:745px;width:230px;gap:20px">
    <article class="milestone">
      <h2>Reconciliation Action<br>Plan (RAP)</h2>
      <p>Marrowfen’s Reflect RAP developed &amp; endorsed</p>
    </article>
    <article class="milestone">
      <h2>Client Advisory Group</h2>
      <p>Marrowfen’s Client Advisory Group commences</p>
    </article>
    <article class="milestone">
      <h2>E-Learning Platform</h2>
      <p>Marrowfen e-learning platform launched</p>
    </article>
    <article class="milestone">
      <h2>Spectrum Tick</h2>
      <p>Marrowfen achieves Spectrum Tick accreditation</p>
    </article>
  </section>

</main>
</body>
</html>
```